Brambury Logistics

Create a modern, simple, Elegant business card design for my business.

Services: Tamo Trucks, Transport, Contract Logistics,

Industry/Entity Type

Business

Contact Information for Business Card

Include all details same as old card plus new website address: www.bramburylogistics.com.au

Requirements
Must have
• Similar colors to Logo.

```html
<!DOCTYPE html>
<html lang="en">
<head>
<meta charset="utf-8">
<title>Brambury Logistics – Business Card</title>
<link rel="stylesheet" href="https://fonts.googleapis.com/css2?family=Open+Sans:wght@400;600;700&display=swap">
<style>
  :root {
    --stage: #3a3a3a;
    --card-black: #0d0d0d;
    --card-black-soft: #1c1c1c;
    --card-white: #ffffff;
    --brand-blue: #1a9ad6;
    --brand-grey: #8a8d91;
    --text-dark: #1a1a1a;
    --text-light: #f2f2f2;
  }
  * { box-sizing: border-box; margin: 0; padding: 0; }
  html, body {
    width: 1200px; height: 950px; overflow: hidden;
    background: var(--stage);
    font-family: "Open Sans", Arial, sans-serif;
  }
  .canvas {
    position: relative; width: 1200px; height: 950px;
    display: flex; flex-direction: column; align-items: center; justify-content: center; gap: 50px;
  }
  .card {
    position: relative; width: 700px; height: 400px; overflow: hidden;
    box-shadow: 0 12px 30px rgba(0,0,0,.45);
  }
  .card svg.shapes { position: absolute; inset: 0; }

  /* Back side */
  .card-back {
    background: linear-gradient(135deg, var(--card-black-soft) 0%, var(--card-black) 60%);
    color: var(--text-light);
    display: flex; flex-direction: column; align-items: center; justify-content: center;
    text-align: center;
  }
  .brand-name { font-weight: 600; color: var(--brand-grey); letter-spacing: .5px; line-height: 1; }
  .card-back .brand-name { font-size: 48px; margin-bottom: 44px; }
  .services-title { font-weight: 700; font-size: 20px; margin-bottom: 6px; }
  .services-list { font-size: 17px; }

  /* Front side */
  .card-front { background: var(--card-white); }
  .card-front .brand-name { position: absolute; left: 44px; top: 66px; font-size: 46px; }
  .person { position: absolute; left: 110px; top: 170px; }
  .person-name { font-size: 30px; font-weight: 600; color: var(--brand-blue); line-height: 1.15; }
  .person-role { font-size: 22px; color: var(--text-dark); }
  .contact {
    position: absolute; right: 26px; top: 250px; list-style: none;
    color: var(--text-light); font-size: 15px; text-align: right;
  }
  .contact li { display: flex; align-items: center; justify-content: flex-end; gap: 10px; height: 28px; }
  .contact svg { width: 16px; height: 16px; flex: none; }
</style>
</head>
<body>
<main class="canvas">

  <section class="card card-back" aria-label="Business card back">
    <div class="brand-name">Brambury Logistics</div>
    <p class="services-title">Services:</p>
    <p class="services-list">Tamo Trucks / Transport / Contract Logistics</p>
  </section>

  <section class="card card-front" aria-label="Business card front">
    <svg class="shapes" viewBox="0 0 700 400" preserveAspectRatio="none" aria-hidden="true">
      <defs>
        <linearGradient id="greyBand" x1="0" y1="0" x2="1" y2="0">
          <stop offset="0" stop-color="#e4e5e6"/>
          <stop offset="1" stop-color="#a9acaf"/>
        </linearGradient>
        <linearGradient id="darkPanel" x1="0" y1="1" x2="1" y2="0">
          <stop offset="0" stop-color="#1e1e1e"/>
          <stop offset="1" stop-color="#070707"/>
        </linearGradient>
      </defs>
      <path d="M0 350 C90 362 160 378 215 400 L0 400 Z" fill="url(#greyBand)"/>
      <path d="M230 400 L660 0 L700 0 L700 400 Z" fill="url(#darkPanel)"/>
      <path d="M198 400 L648 0 L662 0 L232 400 Z" fill="var(--brand-blue)"/>
    </svg>

    <div class="brand-name">Brambury Logistics</div>

    <div class="person">
      <p class="person-name">Liam Carter</p>
      <p class="person-role">CEO/Founder</p>
    </div>

    <ul class="contact">
      <li>0400 123 456
        <svg viewBox="0 0 18 18"><rect x="5" y="1" width="8" height="16" rx="1.5" fill="none" stroke="var(--brand-blue)" stroke-width="1.6"/><circle cx="9" cy="14.3" r="1" fill="var(--brand-blue)"/></svg>
      </li>
      <li>liam@bramburylogistics.com.au
        <svg viewBox="0 0 18 18"><rect x="1" y="4" width="16" height="11" fill="var(--brand-blue)"/><path d="M1 4 L9 10 L17 4" fill="none" stroke="var(--card-black)" stroke-width="1.4"/></svg>
      </li>
      <li>www.bramburylogistics.com.au
        <svg viewBox="0 0 18 18"><circle cx="9" cy="9" r="7.5" fill="var(--brand-blue)"/><path d="M1.5 9 H16.5 M9 1.5 C5.5 5 5.5 13 9 16.5 M9 1.5 C12.5 5 12.5 13 9 16.5" fill="none" stroke="var(--card-black)" stroke-width="1.1"/></svg>
      </li>
    </ul>
  </section>

</main>
</body>
</html>
```